Stationery Design Task - Stationary, memo and report templates for professional services company

Looking for someone to update stationary design but just as importantly come up with a template for reports and memos for use in our consulting firm. Would also like some brand use guidelines to be able to share with our whole team. We have an existing logo that we like. Need to update with a more contemporary look so that our deliverables to clients look good and professional yet stylish. This is for business to business communications. No need for envelope design. Important to have design for multiple pages, i.e. first page of a report and then 2nd page. Need to use in MS word documents so must be easy to use and replicate. Don't want something overly complex. Clean, fresh looking is best.

Industry/Entity Type

Information Technology

Font styles to use
Sans Serif

Colors
33a6d7
0792cd
85cae6
cee9f5
cedeed
85abd2
3377b5
0455a3

Requirements
Must have
• Clean look but with a little style or pop. Something that can easily be used in word documents. Need to have page styles that have a first page of a report (not a cover page) and then secondary page.
Nice to have
• - Although the dark blue is our primary color. Might be willing to look at some accent color as well.
Should not have
• Not just our logo on the page with a color bar.

```html
<!DOCTYPE html>
<html lang="en">
<head>
<meta charset="utf-8">
<title>Lumen Systems Stationery Set</title>
<link rel="stylesheet" href="https://fonts.googleapis.com/css2?family=Roboto:wght@400;500;700;900&family=Questrial&display=swap">
<style>
  :root {
    --backdrop: #616161;
    --blue-deep: #0455a3;
    --blue-primary: #0792cd;
    --blue-mid: #33a6d7;
    --blue-light: #85cae6;
    --blue-pale: #cee9f5;
    --ink-grey: #646464;
    --text-grey: #555555;
    --rule-grey: #7a7a7a;
    --paper: #ffffff;
    --paper-shade: #d6d6d6;
  }
  * { box-sizing: border-box; margin: 0; padding: 0; }
  html, body {
    width: 1200px;
    height: 578px;
    overflow: hidden;
    background: var(--backdrop);
  }
  .canvas {
    position: relative;
    width: 1200px;
    height: 578px;
    font-family: "Roboto", Arial, sans-serif;
  }
  .page {
    position: absolute;
    top: 52px;
    height: 476px;
    overflow: hidden;
    box-shadow: 0 1px 4px rgba(0,0,0,0.25);
  }

  /* Brand name block */
  .brand { position: absolute; display: flex; align-items: center; }
  .brand-dot {
    border-radius: 50%;
    background: var(--blue-primary);
    flex: none;
  }
  .brand-name {
    font-family: "Roboto", Arial, sans-serif;
    font-weight: 700;
    color: var(--blue-primary);
    line-height: 1;
    white-space: nowrap;
  }

  /* Report cover */
  .report-cover {
    left: 61px;
    width: 338px;
    background: linear-gradient(180deg, #ffffff 0%, #ececec 45%, var(--paper-shade) 100%);
  }
  .cover-accent {
    position: absolute;
    left: 0;
    top: 0;
    width: 130px;
    height: 476px;
  }
  .report-cover .brand { left: 108px; top: 48px; gap: 10px; }
  .report-cover .brand-dot { width: 32px; height: 32px; }
  .report-cover .brand-name { font-size: 20px; }
  .report-title {
    position: absolute;
    left: 118px;
    width: 206px;
    top: 182px;
    text-align: center;
    font-family: "Roboto", Arial, sans-serif;
    font-weight: 900;
    font-size: 32px;
    line-height: 0.95;
    color: var(--ink-grey);
    letter-spacing: 0.2px;
  }
  .prepared-block {
    position: absolute;
    left: 138px;
    top: 302px;
    width: 140px;
    height: 38px;
    border-top: 1px solid var(--rule-grey);
    border-bottom: 1px solid var(--rule-grey);
    text-align: center;
  }
  .prepared-label {
    margin-top: 5px;
    font-weight: 700;
    font-size: 11.5px;
    color: var(--ink-grey);
    letter-spacing: 0.2px;
  }
  .prepared-name {
    margin-top: 2px;
    font-weight: 500;
    font-size: 10px;
    color: var(--blue-primary);
    letter-spacing: 0.3px;
  }
  .validity {
    position: absolute;
    top: 436px;
    text-align: center;
    font-family: "Questrial", Arial, sans-serif;
    font-size: 8px;
    line-height: 1.35;
    color: #3d3d3d;
  }
  .validity-label { color: var(--blue-primary); letter-spacing: 0.2px; }
  .validity--issued { left: 60px; width: 90px; }
  .validity--until { left: 218px; width: 90px; top: 434px; }

  /* Letterhead */
  .letterhead {
    left: 434px;
    width: 339px;
    background: linear-gradient(180deg, #ffffff 0%, #f6f6f6 60%, #efefef 100%);
  }
  .letterhead .brand { left: 82px; top: 30px; gap: 8px; }
  .letterhead .brand-dot { width: 26px; height: 26px; }
  .letterhead .brand-name { font-size: 18px; }
  .letter-body {
    position: absolute;
    left: 30px;
    top: 133px;
    width: 281px;
    font-family: "Questrial", Arial, sans-serif;
    color: var(--text-grey);
  }
  .salutation { font-size: 9px; margin-bottom: 12px; color: #444; }
  .letter-body p {
    font-size: 4.9px;
    line-height: 7.1px;
    margin-bottom: 6px;
    text-align: justify;
  }
  .closing { font-size: 5px; margin-top: 10px; }
  .signature {
    position: absolute;
    left: 30px;
    top: 326px;
    width: 76px;
    height: 30px;
  }
  .letter-footer {
    position: absolute;
    left: 0;
    bottom: 0;
    width: 339px;
    height: 72px;
  }
  .contact-bar {
    position: absolute;
    left: 0;
    top: 394px;
    width: 339px;
    height: 14px;
    background: var(--blue-primary);
    color: #ffffff;
    font-family: "Roboto", Arial, sans-serif;
    font-weight: 500;
    font-size: 5.4px;
    line-height: 14px;
    text-align: center;
    letter-spacing: 0.15px;
  }
  .contact-bar .gap { display: inline-block; width: 8px; }

  /* Continuation page */
  .continuation {
    left: 806px;
    width: 340px;
    background: linear-gradient(90deg, #d8d8d8 0%, #ededed 22%, #fafafa 55%, #ffffff 100%);
  }
  .continuation .brand-dot {
    position: absolute;
    left: 294px;
    top: 420px;
    width: 30px;
    height: 30px;
  }
</style>
</head>
<body>
<div class="canvas">

  <!-- Report cover page -->
  <section class="page report-cover">
    <svg class="cover-accent" viewBox="0 0 130 476" role="img" aria-label="Blue geometric side pattern" preserveAspectRatio="none">
      <defs>
        <linearGradient id="coverAccentFill" x1="0" y1="0" x2="1" y2="1">
          <stop offset="0" stop-color="#0792cd"/>
          <stop offset="1" stop-color="#0455a3"/>
        </linearGradient>
      </defs>
      <path d="M0 0 H40 C80 80 112 170 112 250 C112 340 70 410 24 476 H0 Z" fill="url(#coverAccentFill)"/>
    </svg>

    <div class="brand">
      <span class="brand-dot"></span>
      <span class="brand-name">LUMEN SYSTEMS</span>
    </div>

    <h1 class="report-title">REPORT<br>TITLE HERE</h1>

    <div class="prepared-block">
      <div class="prepared-label">REPORT PREPARED BY</div>
      <div class="prepared-name">YOUR NAME HERE</div>
    </div>

    <div class="validity validity--issued">
      <div class="validity-label">PROPOSAL ISSUED</div>
      <div>SEP 19,2018</div>
    </div>
    <div class="validity validity--until">
      <div class="validity-label">PROPOSAL VALID TO</div>
      <div>SEP 19,2019</div>
    </div>
  </section>

  <!-- Letterhead page -->
  <section class="page letterhead">
    <div class="brand">
      <span class="brand-dot"></span>
      <span class="brand-name">LUMEN SYSTEMS</span>
    </div>

    <div class="letter-body">
      <div class="salutation">Dear Mr. Hale,</div>
      <p>Thank you for meeting with our team last week to discuss the planned upgrade of your network and support services. We have reviewed your current systems, spoken with your staff and prepared a short outline of the steps we recommend. This letter summarises our findings and sets out the next actions we propose to take together over the coming quarter.</p>
      <p>Our first priority is to replace the ageing servers in your main office and move shared files to a secure hosted platform. This work can be completed in stages so that daily operations are not interrupted. We will provide a detailed schedule, clear costs and a single point of contact for every stage of the project.</p>
      <p>Once the new systems are in place, we suggest a short training programme for your staff along with a monthly review of performance and security. These reviews help us spot issues early and keep your technology aligned with the goals of your business as it continues to grow.</p>
      <p>Please let us know if you have any questions about this proposal. We would be glad to arrange a follow-up call at a time that suits you and your team.</p>
      <div class="closing">Sincerely,</div>
    </div>

    <svg class="signature" viewBox="0 0 76 30" role="img" aria-label="Handwritten signature">
      <rect x="0" y="6" width="76" height="20" rx="3" fill="#cedeed" opacity="0.6"/>
    </svg>

    <svg class="letter-footer" viewBox="0 0 339 72" role="img" aria-label="Light blue geometric footer pattern" preserveAspectRatio="none">
      <defs>
        <linearGradient id="footerFill" x1="0" y1="0" x2="1" y2="0">
          <stop offset="0" stop-color="#85cae6"/>
          <stop offset="0.55" stop-color="#33a6d7"/>
          <stop offset="1" stop-color="#0792cd"/>
        </linearGradient>
        <linearGradient id="footerFade" x1="0" y1="0" x2="0" y2="1">
          <stop offset="0" stop-color="#fff" stop-opacity="0"/>
          <stop offset="0.35" stop-color="#fff" stop-opacity="1"/>
        </linearGradient>
        <mask id="footerMask">
          <rect width="339" height="72" fill="url(#footerFade)"/>
        </mask>
      </defs>
      <rect width="339" height="72" fill="url(#footerFill)" mask="url(#footerMask)"/>
    </svg>

    <div class="contact-bar">
      1420 CEDAR ROW, LAKEPORT, OREGON 97120<span class="gap"></span>555 014 2290 | INFO@LUMENSYSTEMS.COM
    </div>
  </section>

  <!-- Continuation page -->
  <section class="page continuation">
    <span class="brand-dot"></span>
  </section>

</div>
</body>
</html>
```